Facebook Ad

I am looking for an ad for my moving company that highlights are long distance moving service. I want the ad to also mention the we give free in-home quotes. Also Ithe ad will have a call no action at the bottom so it will not need a phone number but I would like nice picture.

```html
<!DOCTYPE html>
<html lang="en">
<head>
<meta charset="UTF-8">
<title>Long Distance Moving Ad</title>
<link rel="stylesheet" href="https://fonts.googleapis.com/css2?family=Bebas+Neue&family=Montserrat:wght@500;700;800&display=swap">
<style>
  :root {
    --page: #ffffff;
    --blue-deep: #0a3a9e;
    --blue: #0f4fc4;
    --blue-light: #2f6fd8;
    --white: #ffffff;
    --orange: #f28a2e;
    --orange-band: rgba(242, 138, 46, 0.85);
    --pink: #ee2e5a;
    --logo-bg: #f1f2f4;
  }
  html, body {
    margin: 0;
    padding: 0;
    width: 1200px;
    height: 1200px;
    overflow: hidden;
    background: var(--page);
  }
  .ad {
    position: relative;
    width: 1200px;
    height: 1200px;
    background: var(--page);
  }
  .panel {
    position: absolute;
    left: 38px;
    top: 38px;
    width: 1124px;
    height: 1124px;
    overflow: hidden;
  }
  .photo {
    position: absolute;
    inset: 0;
    background:
      radial-gradient(ellipse at 80% 75%, rgba(90, 120, 190, 0.55), transparent 55%),
      radial-gradient(ellipse at 30% 70%, rgba(70, 110, 200, 0.5), transparent 50%),
      linear-gradient(180deg, var(--blue) 0%, var(--blue-light) 55%, var(--blue-deep) 100%);
  }
  .headline {
    position: absolute;
    left: 64px;
    top: 100px;
    margin: 0;
    font-family: "Bebas Neue", "Oswald", sans-serif;
    font-weight: 400;
    font-size: 130px;
    line-height: 118px;
    color: var(--white);
    letter-spacing: 1px;
  }
  .divider {
    position: absolute;
    left: 74px;
    top: 487px;
    width: 186px;
    height: 5px;
    background: var(--orange);
  }
  .offer {
    position: absolute;
    left: 76px;
    top: 535px;
    margin: 0;
    font-family: "Montserrat", sans-serif;
    font-weight: 500;
    font-size: 55px;
    line-height: 72px;
    color: var(--white);
    letter-spacing: 1px;
  }
  .offer strong { font-weight: 800; }
  .brand {
    position: absolute;
    left: 769px;
    top: 32px;
    width: 310px;
    height: 310px;
    border-radius: 50%;
    background: var(--logo-bg);
    display: flex;
    align-items: center;
    justify-content: center;
    box-shadow: 0 4px 14px rgba(0, 0, 0, 0.18);
  }
  .brand-name {
    font-family: "Montserrat", sans-serif;
    font-weight: 800;
    font-size: 30px;
    line-height: 36px;
    color: var(--blue);
    text-align: center;
    text-transform: uppercase;
  }
  .services {
    position: absolute;
    left: 0;
    top: 904px;
    width: 1124px;
    height: 70px;
    background: var(--orange-band);
    display: flex;
    align-items: center;
    padding-left: 80px;
    box-sizing: border-box;
    font-family: "Montserrat", sans-serif;
    font-weight: 700;
    font-size: 38px;
    color: var(--white);
    white-space: nowrap;
  }
  .services .dot { margin: 0 16px; }
  .cta {
    position: absolute;
    left: 389px;
    top: 1016px;
    width: 346px;
    height: 83px;
    border-radius: 12px;
    background: var(--pink);
    display: flex;
    align-items: center;
    justify-content: center;
    font-family: "Montserrat", sans-serif;
    font-weight: 800;
    font-size: 33px;
    color: var(--white);
  }
</style>
</head>
<body>
  <div class="ad">
    <div class="panel">
      <div class="photo" role="img" aria-label="Photo of movers in blue uniforms loading boxes into a truck while a couple watches, under a blue tint"></div>

      <h1 class="headline">Need<br>Long Distance<br>Moving Company</h1>
      <div class="divider"></div>
      <p class="offer">TAKE ADVANTAGE<br>OUR <strong>FREE IN-HOME</strong><br><strong>QUOTES</strong></p>

      <div class="brand">
        <div class="brand-name">Harbor Lane<br>Moving</div>
      </div>

      <div class="services">
        RESIDENTIAL<span class="dot">•</span>LONG DISTANCE<span class="dot">•</span>COMMERCIAL
      </div>

      <div class="cta">CALL TO ACTION</div>
    </div>
  </div>
</body>
</html>
```